Quarrydeen Fintech Product Infographic

Quarrydeen is an established Fintech business, supplying complex financial software to banks and building societies.

We currently have a picture/infographic to show each of our 11 different software products in a single image. Each product can be installed on its own as a standalone application or if multiple products are installed they will share data.

The key message for our infographic is to convey the integration via a shared database.

The attached diagram is what we currently use which is to give you an idea of the message we are trying to give, but we are not tied to this format and are looking for this diagram to be reimagined.

We will look to use our new chosen design on printed media such as A4 Data sheets an example of which is attached.

For more information on our products please refer to www.quarrydeen.co.uk/products

```html
<!DOCTYPE html>
<html lang="en">
<head>
<meta charset="utf-8">
<title>Quarrydeen Fintech Product Infographic</title>
<link rel="stylesheet" href="https://fonts.googleapis.com/css2?family=Barlow:wght@600;700&family=Oswald:wght@500&display=swap">
<style>
  :root {
    --bg: #ffffff;
    --ring-outer: #dedede;
    --ring-inner: #efefef;
    --connector: #cbcbcb;
    --label: #2b2525;
    --performance: #b4498c;
    --performance-dot: #c879a9;
    --finance: #1f6fb7;
    --finance-dot: #4aa6e0;
    --risk: #ef9a22;
    --risk-dot: #f2b35e;
    --regulatory: #1a9a4a;
    --regulatory-dot: #3db36d;
  }
  html, body {
    margin: 0;
    padding: 0;
    overflow: hidden;
    background: var(--bg);
  }
  .canvas {
    width: 1200px;
    height: 849px;
    display: block;
  }
  .connector { stroke: var(--connector); stroke-width: 10; stroke-linecap: butt; }
  .ring { fill: none; stroke: var(--ring-outer); stroke-width: 14; }
  .ring-inner { fill: none; stroke: var(--ring-inner); stroke-width: 6; }
  .label {
    font-family: "Barlow", sans-serif;
    font-weight: 600;
    font-size: 16px;
    fill: var(--label);
  }
  .hub-title {
    font-family: "Barlow", sans-serif;
    font-weight: 700;
    font-size: 46px;
    fill: var(--label);
    letter-spacing: 0.5px;
  }
  .group-title {
    font-family: "Oswald", sans-serif;
    font-weight: 500;
    font-size: 24px;
    text-anchor: middle;
  }
  .performance .dot { fill: var(--performance-dot); }
  .performance .group-title { fill: var(--performance); }
  .finance .dot { fill: var(--finance-dot); }
  .finance .group-title { fill: var(--finance); }
  .risk .dot { fill: var(--risk-dot); }
  .risk .group-title { fill: var(--risk); }
  .regulatory .dot { fill: var(--regulatory-dot); }
  .regulatory .group-title { fill: var(--regulatory); }
  .dot-halo { opacity: 0.45; }
</style>
</head>
<body>
<svg class="canvas" viewBox="0 0 1200 849" xmlns="http://www.w3.org/2000/svg">
  <defs>
    <linearGradient id="hub-fill" x1="0" y1="0" x2="1" y2="1">
      <stop offset="0" stop-color="#dcebf8"/>
      <stop offset="1" stop-color="#9fc3e6"/>
    </linearGradient>
  </defs>

  <!-- connectors -->
  <line class="connector" x1="330" y1="229" x2="470" y2="327"/>
  <line class="connector" x1="873" y1="239" x2="713" y2="348"/>
  <line class="connector" x1="323" y1="626" x2="517" y2="488"/>
  <line class="connector" x1="884" y1="618" x2="729" y2="516"/>

  <!-- central shared database -->
  <g class="hub">
    <rect x="421" y="279" width="368" height="263" rx="18" fill="url(#hub-fill)" role="img" aria-label="Illustration of server racks, a laptop showing data charts, and small bar and pie charts representing the shared database"/>
    <rect x="427" y="402" width="362" height="50" fill="#ffffff" opacity="0.8"/>
    <text class="hub-title" x="608" y="443" text-anchor="middle">SHARE DATA</text>
  </g>

  <!-- performance -->
  <g class="performance">
    <circle class="ring" cx="251" cy="184" r="94"/>
    <circle class="ring-inner" cx="251" cy="184" r="85"/>
    <rect x="205" y="134" width="92" height="72" rx="10" fill="#f1dbe8" role="img" aria-label="Performance gauge icon with a person"/>
    <text class="group-title" x="253" y="230" textLength="102" lengthAdjust="spacingAndGlyphs">PERFORMACE</text>
    <circle class="dot dot-halo" cx="264" cy="95" r="13"/><circle class="dot" cx="264" cy="95" r="9"/>
    <circle class="dot dot-halo" cx="328" cy="228" r="13"/><circle class="dot" cx="328" cy="228" r="9"/>
    <circle class="dot dot-halo" cx="161" cy="200" r="13"/><circle class="dot" cx="161" cy="200" r="9"/>
    <text class="label" x="280" y="88">Financial Planning</text>
    <text class="label" x="358" y="202">Funds Transfer</text>
    <text class="label" x="358" y="223">Pricing</text>
    <text class="label" x="79" y="220">Business</text>
    <text class="label" x="79" y="241">Intellegence</text>
  </g>

  <!-- finance -->
  <g class="finance">
    <circle class="ring" cx="950" cy="183" r="94"/>
    <circle class="ring-inner" cx="950" cy="183" r="85"/>
    <rect x="907" y="131" width="88" height="72" rx="10" fill="#dbe9f6" role="img" aria-label="Financial document icon with coins and bar chart"/>
    <text class="group-title" x="948" y="229" textLength="65" lengthAdjust="spacingAndGlyphs">FINANCE</text>
    <circle class="dot dot-halo" cx="903" cy="105" r="13"/><circle class="dot" cx="903" cy="105" r="9"/>
    <circle class="dot dot-halo" cx="1039" cy="167" r="13"/><circle class="dot" cx="1039" cy="167" r="9"/>
    <circle class="dot dot-halo" cx="891" cy="252" r="13"/><circle class="dot" cx="891" cy="252" r="9"/>
    <text class="label" x="757" y="98">Financial Ledgers</text>
    <text class="label" x="1058" y="181">Hedge</text>
    <text class="label" x="1058" y="202">Accounting</text>
    <text class="label" x="854" y="293">Effective</text>
    <text class="label" x="854" y="314">Interest Rates</text>
  </g>

  <!-- risk -->
  <g class="risk">
    <circle class="ring" cx="242" cy="680" r="94"/>
    <circle class="ring-inner" cx="242" cy="680" r="85"/>
    <rect x="195" y="618" width="92" height="89" rx="10" fill="#fde6c4" role="img" aria-label="Risk icon with bar chart and warning sign"/>
    <text class="group-title" x="239" y="733" textLength="36" lengthAdjust="spacingAndGlyphs">RISK</text>
    <circle class="dot dot-halo" cx="170" cy="623" r="13"/><circle class="dot" cx="170" cy="623" r="9"/>
    <circle class="dot dot-halo" cx="319" cy="727" r="13"/><circle class="dot" cx="319" cy="727" r="9"/>
    <text class="label" x="122" y="620">ALM</text>
    <text class="label" x="342" y="738">Treasury</text>
  </g>

  <!-- regulatory -->
  <g class="regulatory">
    <circle class="ring" cx="955" cy="682" r="94"/>
    <circle class="ring-inner" cx="955" cy="682" r="85"/>
    <rect x="915" y="631" width="82" height="66" rx="10" fill="#d8efe0" role="img" aria-label="Regulatory document icon with magnifying glass"/>
    <text class="group-title" x="955" y="723" textLength="98" lengthAdjust="spacingAndGlyphs">REGULATORY</text>
    <circle class="dot dot-halo" cx="972" cy="591" r="13"/><circle class="dot" cx="972" cy="591" r="9"/>
    <circle class="dot dot-halo" cx="869" cy="719" r="13"/><circle class="dot" cx="869" cy="719" r="9"/>
    <circle class="dot dot-halo" cx="1027" cy="727" r="13"/><circle class="dot" cx="1027" cy="727" r="9"/>
    <text class="label" x="899" y="570">Taxation Reporting</text>
    <text class="label" x="773" y="717">Regulatory</text>
    <text class="label" x="773" y="738">Reporting</text>
    <text class="label" x="1031" y="767">FSCS SCV</text>
  </g>
</svg>
</body>
</html>
```